Criação de Layout para Website para alimenticio
" A Ve Brinola é uma empresa que produz doces finos para eventos (corporativos e sociais), cujo público alvo são consumidores que valorizam um produto de qualidade e diferenciado. "

```html
<!DOCTYPE html>
<html lang="pt-BR">
<head>
<meta charset="utf-8">
<title>Ve Brinola — Doces Finos</title>
<link href="https://fonts.googleapis.com/css2?family=Open+Sans:ital,wght@0,400;0,600;0,700;1,400&display=swap" rel="stylesheet">
<style>
:root{
  --brown:#5b4f42;
  --brown-dark:#4a3f35;
  --mint:#c6eaed;
  --page:#ffffff;
  --panel:#f7f7f7;
  --line:#d6d6d6;
  --text:#5f5a55;
  --navy:#1f2436;
  --field:#e9ecef;
}
*{box-sizing:border-box;margin:0;padding:0}
html,body{width:771px;height:1200px;overflow:hidden;background:var(--page)}
body{position:relative;font-family:"Open Sans",sans-serif;color:var(--text)}
.abs{position:absolute}

/* header */
.social{left:622px;top:42px;display:flex;gap:4px}
.social span{width:24px;height:24px;border-radius:50%;background:var(--brown);display:block}
.search{left:561px;top:71px;width:168px;height:17px;background:var(--field);border:1px solid #ddd}
.search-btn{right:-1px;top:-1px;width:19px;height:17px;background:var(--brown)}
.nav{left:40px;top:96px;width:690px;height:29px;background:var(--brown);display:flex;align-items:center;color:#fff;font-weight:700;font-size:11.5px}
.nav a{color:#fff;text-decoration:none;height:29px;display:flex;align-items:center;justify-content:center;border-right:1px solid #6f6356}
.nav .menu{width:44px;border:none}
.nav .home{width:70px}
.nav .about{width:100px;background:var(--mint);color:var(--brown-dark)}
.nav .spacer{flex:1;border:none}
.nav .products{width:94px;border-left:1px solid #6f6356}
.nav .contact{width:82px;border:none}
.brand{left:282px;top:20px;width:212px;height:160px;background:var(--page);border-radius:16px;display:flex;align-items:center;justify-content:center;gap:8px}
.brand .dot{width:22px;height:22px;border-radius:50%;background:var(--mint)}
.brand .name{font-size:30px;font-weight:700;color:var(--brown)}

/* main panel */
.panel{left:40px;top:130px;width:690px;height:946px;background:var(--panel);border:1px solid #e2e2e2}
.thumb{left:48px;width:210px;height:53px}
.hero{left:264px;top:137px;width:460px;height:287px;background:linear-gradient(180deg,#8a6a3a 0%,#5a2e1c 45%,#3a2218 100%)}
.hero-band{left:264px;top:281px;width:460px;height:105px;background:rgba(40,30,22,.78)}
.hero-title{left:275px;top:287px;color:#fff;font-size:19px;font-weight:400}
.hero-copy{left:275px;top:320px;color:#e9e5e0;font-size:9.2px;line-height:15px;width:440px}
.hero-copy b{font-weight:700}
.btn-mint{left:274px;top:355px;width:65px;height:22px;background:var(--mint);color:var(--brown);font-size:8.5px;font-weight:600;display:flex;align-items:center;justify-content:center}
.btn-ghost{left:345px;top:355px;width:65px;height:22px;border:1px solid #fff;border-radius:2px;color:#fff;font-size:8.5px;font-weight:600;display:flex;align-items:center;justify-content:center}
.dots{left:686px;top:374px;display:flex;gap:4px}
.dots i{width:7px;height:7px;border:1px solid #fff;border-radius:50%;display:block}
.dots i.on{background:#fff}

.rule{left:50px;width:671px;height:1px;background:var(--line)}
.h-section{font-weight:700;color:var(--brown);font-size:15.5px;letter-spacing:.4px}
.about-logo{left:57px;top:505px;width:149px;height:149px;background:#fff;border:1px solid #eee;display:flex;align-items:center;justify-content:center;gap:5px}
.about-logo .dot{width:12px;height:12px;border-radius:50%;background:var(--mint)}
.about-logo .name{font-size:17px;font-weight:700;color:var(--brown)}
.about-copy{left:216px;top:505px;width:480px;font-size:12.4px;line-height:12.8px;color:#6b6662}
.about-copy p{margin-bottom:12.8px}
.about-copy b{color:var(--brown);font-weight:700}

.gallery-main{left:56px;top:796px;width:277px;height:184px;background:linear-gradient(180deg,#9a7b45 0%,#6b3a22 50%,#3d2a20 100%)}
.g-thumb{top:985px;height:66px}
.arrow{top:1000px;width:33px;height:33px;border-radius:50%;background:#2a2522}
.comments-label{left:380px;top:790px;font-style:italic;font-size:12.5px;color:#6b6662}
.avatar{width:38px;height:38px;border-radius:50%;background:#d8d4cf;border:2px solid #fff;box-shadow:0 0 0 1px #ddd}
.bubble{width:108px;height:65px;background:var(--brown);border-radius:5px;color:#fff;padding:3px 5px}
.bubble .who{font-size:8.5px;line-height:11px}
.bubble .date{font-size:5.5px;font-weight:700;line-height:8px}
.bubble .msg{font-size:6.2px;line-height:7px;margin-top:2px}

/* footer */
.f-col h3{font-size:19px;font-weight:700;color:var(--brown);line-height:22px}
.f-col p{font-size:11px;font-weight:700;color:var(--navy);line-height:13.5px}
.f-btn{height:15px;background:var(--mint);color:var(--brown);font-size:8px;display:flex;align-items:center;justify-content:center}
</style>
</head>
<body>

<header>
  <div class="abs social" aria-label="Redes sociais"><span></span><span></span><span></span><span></span></div>
  <div class="abs search"><div class="abs search-btn">
    <svg width="19" height="17" viewBox="0 0 19 17"><circle cx="9" cy="7.5" r="2.6" fill="none" stroke="#fff" stroke-width="1.3"/><line x1="11" y1="9.5" x2="13" y2="11.5" stroke="#fff" stroke-width="1.4"/></svg>
  </div></div>
  <nav class="abs nav">
    <a class="menu" href="#"><svg width="16" height="12" viewBox="0 0 16 12"><rect y="0" width="16" height="2" fill="#fff"/><rect y="5" width="16" height="2" fill="#fff"/><rect y="10" width="16" height="2" fill="#fff"/></svg></a>
    <a class="home" href="#">HOME</a>
    <a class="about" href="#">QUEM SOMOS</a>
    <span class="spacer"></span>
    <a class="products" href="#">PRODUTOS</a>
    <a class="contact" href="#">CONTATO</a>
  </nav>
  <div class="abs brand"><span class="dot"></span><span class="name">Ve Brinola</span></div>
</header>

<main>
  <div class="abs panel"></div>

  <div class="abs thumb" style="top:137px;background:linear-gradient(90deg,#6b3a22,#c9b9a0,#7a3d22)" role="img" aria-label="Mesa de doces com bolo branco e arranjos florais"></div>
  <div class="abs thumb" style="top:194px;background:linear-gradient(90deg,#b75d6f,#e79aa8,#8c4a57)" role="img" aria-label="Bolo rosa decorado com flores"></div>
  <div class="abs thumb" style="top:253px;background:linear-gradient(90deg,#8c1a1c,#d63a3a,#7a2a2a)" role="img" aria-label="Doces com cerejas em forminhas"></div>
  <div class="abs thumb" style="top:311px;background:linear-gradient(90deg,#8a7a50,#e0b23a,#b8862a)" role="img" aria-label="Doces de maracujá em pequenos copos"></div>
  <div class="abs thumb" style="top:371px;background:linear-gradient(90deg,#c9d28a,#e9c0c8,#c63d6e)" role="img" aria-label="Macarons coloridos"></div>

  <div class="abs hero" role="img" aria-label="Salão de festa com mesa de doces, bolo de casamento e arranjos de flores"></div>
  <div class="abs hero-band"></div>
  <h1 class="abs hero-title">SEJA BEM VINDO !</h1>
  <p class="abs hero-copy">A <b>Ve Brinola</b> é uma empresa que produz doces finos para eventos (corporativos e sociais).<br>Conheça nos melhor clicando no botão “Quem Somos” ou saiba mais sobre nossos serviços</p>
  <a class="abs btn-mint">SAIBA MAIS</a>
  <a class="abs btn-ghost">QUEM SOMOS</a>
  <div class="abs dots"><i></i><i class="on"></i><i></i></div>

  <div class="abs rule" style="top:451px"></div>
  <h2 class="abs h-section" style="left:61px;top:471px">QUEM SOMOS?</h2>
  <div class="abs about-logo"><span class="dot"></span><span class="name">Ve Brinola</span></div>
  <div class="abs about-copy">
    <p>A <b>Ve Brinola</b> é comandada por Helena Vasconti, formada em Gastronomia pelo Instituto Paulista de Culinária e com diversos cursos de especialização em São Paulo e, especificamente em macarons, pela Maison Lévrier de Paris e Atelier de Pâtisserie Rossel.</p>
    <p>O nosso portfólio inclui macarons, chocolates belgas, brigadeiros gourmet, doces finos, bem casados, bolos artísticos, stolens, produtos diet, além das linhas sazonais e doces personalizados. Produzimos também bolos e doces para tornar aquele chá da tarde ainda mais delicioso!</p>
    <p>Os produtos da empresa fizeram parte de eventos corporativos para diversas empresas e adoçaram eventos sociais de renomados espaços.</p>
    <p>Todos os nossos produtos são elaborados através de cuidado processo e os ingredientes primam pela qualidade, originando assim um produto final que busca a excelência e a diferenciação, proporcionando uma experiência gastronômica inesquecível para superar sempre a expectativa dos nossos clientes.</p>
  </div>

  <div class="abs rule" style="top:738px"></div>
  <h2 class="abs h-section" style="left:53px;top:765px">GALERIA / CASOS DE SUCESSO</h2>
  <div class="abs gallery-main" role="img" aria-label="Mesa de doces de casamento em salão decorado com flores"></div>
  <div class="abs g-thumb" style="left:57px;width:88px;background:linear-gradient(135deg,#a0463a,#6b4a34)" role="img" aria-label="Doces de chocolate com frutas vermelhas"></div>
  <div class="abs g-thumb" style="left:149px;width:92px;background:linear-gradient(135deg,#5a3a22,#b08a4a)" role="img" aria-label="Convidados em festa de casamento"></div>
  <div class="abs g-thumb" style="left:245px;width:88px;background:linear-gradient(135deg,#8a6a5a,#c9b3a0)" role="img" aria-label="Bandeja de doces finos"></div>
  <div class="abs arrow" style="left:58px"><svg width="33" height="33" viewBox="0 0 33 33"><polyline points="19,10 13,16.5 19,23" fill="none" stroke="#fff" stroke-width="2.2"/></svg></div>
  <div class="abs arrow" style="left:297px"><svg width="33" height="33" viewBox="0 0 33 33"><polyline points="14,10 20,16.5 14,23" fill="none" stroke="#fff" stroke-width="2.2"/></svg></div>

  <h2 class="abs h-section" style="left:378px;top:765px">CASAMENTO BIANCA &amp; RAFAEL</h2>
  <p class="abs comments-label">COMENTÁRIOS:</p>

  <div class="abs avatar" style="left:379px;top:836px" role="img" aria-label="Foto de perfil de Rafael Dornelas"></div>
  <div class="abs bubble" style="left:424px;top:820px">
    <div class="who">Rafael Dornelas</div>
    <div class="date">08 /08/2014</div>
    <div class="msg">Lorem ipsum dolor sit amet, consectetur adipisicing elit, sed do eiusmod tempor incididunt ut labore et dolore magna aliqua.</div>
  </div>
  <div class="abs avatar" style="left:559px;top:827px" role="img" aria-label="Foto de perfil de Bianca Tavares"></div>
  <div class="abs bubble" style="left:605px;top:827px">
    <div class="who">Bianca Tavares</div>
    <div class="date">08 /08/2014</div>
    <div class="msg">Lorem ipsum dolor sit amet, consectetur adipisicing elit, sed do eiusmod tempor incididunt ut labore et dolore magna aliqua.</div>
  </div>
</main>

<footer>
  <div class="abs f-col" style="left:80px;top:1094px">
    <h3>Atendimento</h3>
    <p>Fone: (11) 90000-3175<br>contato@vebrinola.com.br</p>
  </div>
  <div class="abs f-col" style="left:243px;top:1094px">
    <h3>Onde Estamos</h3>
    <p style="font-size:16px;line-height:19px;padding-left:2px">São Paulo</p>
  </div>
  <div class="abs f-col" style="left:418px;top:1094px">
    <h3>Orçamento</h3>
    <p>Solicite um orçamento<br>sem compromisso.</p>
    <div class="f-btn" style="width:60px;margin-top:2px">SOLICITAR</div>
  </div>
  <div class="abs f-col" style="left:554px;top:1096px">
    <h3>Newslatter</h3>
    <p>Receba nossas novidades</p>
    <div style="display:flex;align-items:center;gap:4px;margin-top:2px">
      <svg width="12" height="10" viewBox="0 0 12 10"><rect x=".5" y="2" width="11" height="7.5" fill="none" stroke="#4a3f35"/><polyline points=".5,2 6,6 11.5,2" fill="none" stroke="#4a3f35"/></svg>
      <span style="display:block;width:106px;height:15px;background:var(--field)"></span>
    </div>
    <div class="f-btn" style="width:60px;margin:4px 0 0 61px">CADASTRAR</div>
  </div>
</footer>

</body>
</html>
```